Android Game Graphics
Puzzle Game Buttons/Background
I'm developing a puzzle game for android and I need a fun/colorful background and several buttons. I have attached sketches of the three screens I need graphics for.
The winning logo must "pop" like the "fuzzy otters" graphics. The graphics need to be fun and colorful, but I have no formal requirements. The game is a clone of the classic game "Glyphwalk". You can see/play the original game here: http://marlowjpenfield.com/android/games/glyphwalk.swf Below I have sketches of the three screens in the game, please make these with colorful graphics and buttons. For the first and second images, make sure the background image has "Quill Quest" somewhere spanning the back. For the third image, the one with the letters, make all of the letters/tiles the same color. Wood color like tilzor would probably be the best, but I'm open to suggestions. Also where "Quill Quest" is on the third image, make some sort of cartoony logo. I was thinking maybe the word formed from some sort of cartoony worm with glasses, but again, it's up to you. Please make all of the buttons, including the letters individually and high res because they will eventually be used on a 10 inch (1280 x 800 resolution tablet). Screen 1: http://img811.pixelcrate.net/i/introscreen1.png/ Screen 2: http://img827.pixelcrate.net/i/selectgame2.png/ Screen 3: http://img573.pixelcrate.net/i/gameplay3.png/ Basically, make the three images above how you think the game and menu should look. The resolution in the attached images is 854 x 480, but make sure you make them for a higher res tablet.

```html
<!DOCTYPE html>
<html lang="en">
<head>
<meta charset="utf-8">
<title>Quill Quest – Gameplay</title>
<link rel="stylesheet" href="https://fonts.googleapis.com/css2?family=Chewy&family=Fredoka:wght@600;700&display=swap">
<style>
:root{
  --sky-top:#bfe6ee;
  --sky-bottom:#7fc6d6;
  --wood-light:#f1cf8a;
  --wood-mid:#e0b068;
  --wood-dark:#b98440;
  --wood-edge:#8d5f27;
  --ink:#2b1a0c;
  --accent-red:#d11414;
  --logo-orange:#f07a12;
  --book-red:#c8323a;
  --book-blue:#3a78c2;
  --book-cream:#f2ead6;
}
*{margin:0;padding:0;box-sizing:border-box}
html,body{width:1200px;height:751px;overflow:hidden}
body{background:#fff}
.screen{position:relative;width:1200px;height:751px;overflow:hidden;
  background:linear-gradient(180deg,var(--sky-top),var(--sky-bottom))}
.backdrop-shelf{position:absolute;left:70px;top:60px;width:620px;height:620px;border-radius:18px;
  background:linear-gradient(160deg,rgba(255,255,255,.35),rgba(255,255,255,.08))}
.tile{position:absolute;width:64px;height:74px;border-radius:7px;
  background:linear-gradient(160deg,var(--wood-light),var(--wood-mid) 70%,var(--wood-dark));
  box-shadow:inset 0 0 0 2px rgba(141,95,39,.35),2px 4px 5px rgba(0,0,0,.3);
  font-family:"Chewy",cursive;color:var(--ink)}
.tile .glyph{position:absolute;left:14px;top:10px;font-size:40px;line-height:1}
.tile .value{position:absolute;right:8px;bottom:8px;font-size:15px;line-height:1}
.books{position:absolute;left:0;top:545px;width:480px;height:206px;
  border-radius:30px 60px 0 0;
  background:linear-gradient(180deg,var(--book-red) 0 38%,var(--book-cream) 38% 46%,var(--book-blue) 46%)}
.logo{position:absolute;left:842px;top:22px;width:334px;height:140px;display:flex;align-items:center;gap:14px}
.logo .dot{width:54px;height:54px;border-radius:50%;background:#5fbf3a;flex:none}
.logo .name{font-family:"Fredoka",sans-serif;font-weight:700;font-size:54px;color:var(--logo-orange);line-height:1}
.panel-btn{position:absolute;left:840px;width:336px;border-radius:8px;
  background:linear-gradient(180deg,var(--wood-light),var(--wood-mid) 75%,var(--wood-dark));
  box-shadow:inset 0 0 0 2px rgba(141,95,39,.45),2px 4px 6px rgba(0,0,0,.28);
  display:flex;align-items:center;justify-content:center;flex-direction:column;
  font-family:"Fredoka",sans-serif;font-weight:700;color:var(--ink);text-transform:uppercase}
.score{top:192px;height:66px;font-size:30px;flex-direction:row;gap:22px}
.score .num{color:var(--accent-red)}
.word{top:268px;height:86px}
.word .label{font-size:20px;line-height:1.1}
.word .value{font-size:32px;color:var(--accent-red);line-height:1.1}
.points{top:362px;height:70px;font-size:34px}
.level{top:440px;height:84px;font-size:34px}
.clear{top:533px;height:82px;width:160px;font-size:28px}
.scramble{top:533px;height:82px;left:1004px;width:172px;font-size:28px}
.submit{top:622px;height:80px;font-size:34px}
</style>
</head>
<body>
<main class="screen">
  <div class="backdrop-shelf" role="img" aria-label="Soft stack of large books in the background"></div>

  <section class="board" aria-label="Letter tiles">
    <div class="tile" style="left:29px;top:120px"><span class="glyph">A</span><span class="value">1</span></div>
    <div class="tile" style="left:29px;top:198px"><span class="glyph">K</span><span class="value">5</span></div>
    <div class="tile" style="left:29px;top:276px"><span class="glyph">U</span><span class="value">1</span></div>
    <div class="tile" style="left:29px;top:354px"><span class="glyph">E</span><span class="value">1</span></div>
    <div class="tile" style="left:29px;top:432px"><span class="glyph">O</span><span class="value">1</span></div>
    <div class="tile" style="left:29px;top:510px"><span class="glyph">Y</span><span class="value">4</span></div>

    <div class="tile" style="left:107px;top:151px"><span class="glyph">B</span><span class="value">3</span></div>
    <div class="tile" style="left:107px;top:229px"><span class="glyph">L</span><span class="value">1</span></div>
    <div class="tile" style="left:107px;top:307px"><span class="glyph">V</span><span class="value">4</span></div>
    <div class="tile" style="left:107px;top:385px"><span class="glyph">F</span><span class="value">4</span></div>
    <div class="tile" style="left:107px;top:463px"><span class="glyph">P</span><span class="value">3</span></div>
    <div class="tile" style="left:107px;top:541px"><span class="glyph">Z</span><span class="value">10</span></div>

    <div class="tile" style="left:185px;top:120px"><span class="glyph">C</span><span class="value">3</span></div>
    <div class="tile" style="left:185px;top:198px"><span class="glyph">M</span><span class="value">3</span></div>
    <div class="tile" style="left:185px;top:276px"><span class="glyph">W</span><span class="value">4</span></div>
    <div class="tile" style="left:185px;top:354px"><span class="glyph">G</span><span class="value">2</span></div>
    <div class="tile" style="left:185px;top:432px"><span class="glyph">Q</span><span class="value">10</span></div>
    <div class="tile" style="left:185px;top:510px"><span class="glyph">A</span><span class="value">1</span></div>

    <div class="tile" style="left:263px;top:151px"><span class="glyph">D</span><span class="value">2</span></div>
    <div class="tile" style="left:263px;top:229px"><span class="glyph">N</span><span class="value">1</span></div>
    <div class="tile" style="left:263px;top:307px"><span class="glyph">X</span><span class="value">8</span></div>
    <div class="tile" style="left:263px;top:385px"><span class="glyph">H</span><span class="value">4</span></div>
    <div class="tile" style="left:263px;top:463px"><span class="glyph">R</span><span class="value">1</span></div>
    <div class="tile" style="left:263px;top:541px"><span class="glyph">B</span><span class="value">3</span></div>

    <div class="tile" style="left:341px;top:120px"><span class="glyph">E</span><span class="value">1</span></div>
    <div class="tile" style="left:341px;top:198px"><span class="glyph">O</span><span class="value">1</span></div>
    <div class="tile" style="left:341px;top:276px"><span class="glyph">Y</span><span class="value">4</span></div>
    <div class="tile" style="left:341px;top:354px"><span class="glyph">I</span><span class="value">1</span></div>
    <div class="tile" style="left:341px;top:432px"><span class="glyph">S</span><span class="value">1</span></div>
    <div class="tile" style="left:341px;top:510px"><span class="glyph">C</span><span class="value">3</span></div>

    <div class="tile" style="left:419px;top:151px"><span class="glyph">F</span><span class="value">4</span></div>
    <div class="tile" style="left:419px;top:229px"><span class="glyph">P</span><span class="value">3</span></div>
    <div class="tile" style="left:419px;top:307px"><span class="glyph">Z</span><span class="value">10</span></div>
    <div class="tile" style="left:419px;top:385px"><span class="glyph">J</span><span class="value">8</span></div>
    <div class="tile" style="left:419px;top:463px"><span class="glyph">T</span><span class="value">1</span></div>
    <div class="tile" style="left:419px;top:541px"><span class="glyph">D</span><span class="value">2</span></div>

    <div class="tile" style="left:497px;top:120px"><span class="glyph">G</span><span class="value">2</span></div>
    <div class="tile" style="left:497px;top:198px"><span class="glyph">Q</span><span class="value">10</span></div>
    <div class="tile" style="left:497px;top:276px"><span class="glyph">A</span><span class="value">1</span></div>
    <div class="tile" style="left:497px;top:354px"><span class="glyph">K</span><span class="value">5</span></div>
    <div class="tile" style="left:497px;top:432px"><span class="glyph">U</span><span class="value">1</span></div>
    <div class="tile" style="left:497px;top:510px"><span class="glyph">E</span><span class="value">1</span></div>

    <div class="tile" style="left:575px;top:151px"><span class="glyph">H</span><span class="value">4</span></div>
    <div class="tile" style="left:575px;top:229px"><span class="glyph">R</span><span class="value">1</span></div>
    <div class="tile" style="left:575px;top:307px"><span class="glyph">B</span><span class="value">3</span></div>
    <div class="tile" style="left:575px;top:385px"><span class="glyph">L</span><span class="value">1</span></div>
    <div class="tile" style="left:575px;top:463px"><span class="glyph">V</span><span class="value">4</span></div>
    <div class="tile" style="left:575px;top:541px"><span class="glyph">F</span><span class="value">4</span></div>

    <div class="tile" style="left:653px;top:120px"><span class="glyph">I</span><span class="value">1</span></div>
    <div class="tile" style="left:653px;top:198px"><span class="glyph">S</span><span class="value">1</span></div>
    <div class="tile" style="left:653px;top:276px"><span class="glyph">C</span><span class="value">3</span></div>
    <div class="tile" style="left:653px;top:354px"><span class="glyph">M</span><span class="value">3</span></div>
    <div class="tile" style="left:653px;top:432px"><span class="glyph">W</span><span class="value">4</span></div>
    <div class="tile" style="left:653px;top:510px"><span class="glyph">G</span><span class="value">2</span></div>

    <div class="tile" style="left:731px;top:151px"><span class="glyph">J</span><span class="value">8</span></div>
    <div class="tile" style="left:731px;top:229px"><span class="glyph">T</span><span class="value">1</span></div>
    <div class="tile" style="left:731px;top:307px"><span class="glyph">D</span><span class="value">2</span></div>
    <div class="tile" style="left:731px;top:385px"><span class="glyph">N</span><span class="value">1</span></div>
    <div class="tile" style="left:731px;top:463px"><span class="glyph">X</span><span class="value">8</span></div>
    <div class="tile" style="left:731px;top:541px"><span class="glyph">H</span><span class="value">4</span></div>
  </section>

  <div class="books" role="img" aria-label="Stack of red and blue books in the lower left corner"></div>

  <header class="logo">
    <span class="dot"></span>
    <span class="name">Quill Quest</span>
  </header>

  <aside class="controls">
    <div class="panel-btn score"><span>Score :</span><span class="num">1250</span></div>
    <div class="panel-btn word"><span class="label">Current word</span><span class="value">Mushroom</span></div>
    <div class="panel-btn points">10 Points</div>
    <div class="panel-btn level">Level 1</div>
    <div class="panel-btn clear">Clear</div>
    <div class="panel-btn scramble">Scramble</div>
    <div class="panel-btn submit">Submit</div>
  </aside>
</main>
</body>
</html>
```